hello! I need a very simple modern business card for a new venture called The Quiet Harbor Retreats. It's the very first Tech-Free retreat in Asia!

The concept is very unique. Basically a group of 12-15 people would go on a 3 to 4 days retreat where no phone or internet is allowed. The first retreat will take place in a beautiful villa in Bali by the sea. It will include yoga, meditation, art & writing workshops, swimming, hiking, cooking, healthy vegetarian meals, etc.

Reason: Thanks for your submissions. I still haven't found exactly what I'm after but the designs that haven't be eliminated are getting close.. Please keep in mind that it should be a simple, modern and upmarket business card. Thanks

Target Market(s)

Both men and women who would like to disconnect from life, computer and phone for 3/4 days. They can be either local or expats but based in Asia (Singapore, Hong Kong).
Client will have to pay for their own flight and then the price is around US$600 for a 3-day retreat including everything (accommodation, food, activities). It means clients already have a good income. They are usually working in marketing, advertising, digital media, public relations.

Industry/Entity Type

Internet

Font styles to use
Other font styles liked:
• anything modern you like

Colors
acd036
9bcb3c
f37022
f68d4d
1b1b1b
333333
acd037

Requirements
Must have
• Name: Lina Vorel
Position: #gadgetdevotee
Company: The Quiet Harbor Retreats (asia should be smaller than the rest)
- Email button - quietharborretreats@mailverra.com
- FriendSpace button - www.friendspace.com/quietharborretreats
- TicketNest button - www.quietharborretreats.ticketnest.com
Nice to have
• You can use my logo attached but it's something I designed quickly on Power Point so it would be nice to include your own version.
Should not have
• anything tacky or girly or childish. thanks

```html
<!DOCTYPE html>
<html lang="en">
<head>
<meta charset="utf-8">
<title>The Quiet Harbor Retreats — Business Card</title>
<link rel="stylesheet" href="https://fonts.googleapis.com/css2?family=Montserrat:wght@300&display=swap">
<style>
  :root {
    --green: #acd036;
    --orange: #f68d4d;
    --ink: #1b1b1b;
    --text: #333333;
    --social: #3b62a8;
    --tickets: #f37022;
    --paper: #ffffff;
    --backdrop: #ffffff;
  }
  * { margin: 0; padding: 0; box-sizing: border-box; }
  html, body {
    width: 1200px; height: 1000px; overflow: hidden;
    background: var(--backdrop);
    font-family: "Montserrat", "Helvetica Neue", Arial, sans-serif;
    font-weight: 300;
  }
  .canvas { position: relative; width: 1200px; height: 1000px; }
  .card {
    position: absolute; left: 290px; width: 632px; height: 365px;
    background: var(--paper);
    box-shadow: 3px 4px 8px rgba(0,0,0,0.35);
  }
  .card--front { top: 103px; }
  .card--back { top: 537px; }
  .rule { position: absolute; height: 2px; background: var(--green); }
  .brand-dot {
    position: absolute; width: 18px; height: 18px; border-radius: 50%;
    background: var(--green);
  }
  .company {
    position: absolute; white-space: nowrap;
    color: var(--ink); font-size: 24px; letter-spacing: 0.2px;
  }
  .holder { position: absolute; right: 35px; text-align: right; }
  .holder__name { color: var(--ink); font-size: 30px; line-height: 32px; letter-spacing: 0.5px; }
  .holder__role { color: var(--orange); font-size: 20px; line-height: 22px; }
  .contacts { position: absolute; right: 33px; top: 220px; list-style: none; }
  .contacts li {
    display: flex; align-items: center; justify-content: flex-end;
    height: 33px; margin-bottom: 1px;
    color: var(--text); font-size: 18.5px; letter-spacing: 0.2px;
  }
  .contacts .icon { width: 32px; height: 30px; margin-left: 14px; flex: none; }
  .icon--square-social { background: var(--social); border-radius: 4px; width: 29px !important; height: 29px !important; margin-right: 2px; }
  .icon--square-tickets { background: var(--tickets); border-radius: 4px; width: 30px !important; height: 30px !important; margin-right: 2px; }
</style>
</head>
<body>
<main class="canvas">

  <section class="card card--front" aria-label="Card front">
    <span class="brand-dot" style="left:104px; top:261px;"></span>
    <p class="company" style="left:192px; top:233px;">The Quiet Harbor Retreats</p>
    <div class="rule" style="left:0; top:269px; width:85px;"></div>
    <div class="rule" style="left:142px; top:269px; width:490px;"></div>
  </section>

  <section class="card card--back" aria-label="Card back">
    <span class="brand-dot" style="left:48px; top:166px;"></span>
    <p class="company" style="left:120px; top:141px;">The Quiet Harbor Retreats</p>
    <div class="holder" style="top:110px;">
      <p class="holder__name">Lina Vorel</p>
      <p class="holder__role">gadgetdevotee</p>
    </div>
    <div class="rule" style="left:0; top:174px; width:30px;"></div>
    <div class="rule" style="left:85px; top:174px; width:547px;"></div>

    <ul class="contacts">
      <li>quietharborretreats@mailverra.com
        <svg class="icon" viewBox="0 0 32 22" aria-label="Email">
          <rect x="0" y="0" width="32" height="22" fill="var(--green)"/>
          <path d="M1 1 L16 13 L31 1 M1 21 L12 10 M31 21 L20 10" fill="none" stroke="#fff" stroke-width="1.6"/>
        </svg>
      </li>
      <li>www.friendspace.com/quietharborretreats
        <span class="icon icon--square-social" aria-label="FriendSpace"></span>
      </li>
      <li>www.quietharborretreats.ticketnest.com
        <span class="icon icon--square-tickets" aria-label="TicketNest"></span>
      </li>
    </ul>
  </section>

</main>
</body>
</html>
```